1 OZ TRANSDERMAL CBD. NOVEL, INNOVATIVE FIRST TIME EVER OF CBD THAT PENETRATES THROUGH SKIN.
BRAND: VELLOR WELLWORKS
NAME: HEMP GLIDE

Target Market(s)

CBD users waiting a smarter way-through the skin. None lost in toilet like other CBD, directly into you within 5 minutes.

Requirements
Must have
• Elegant, bold, natural, NOT THE SAME OLD CBD. Jump off shelf.
Should not have
• Boring "me-too" labels.

```html
<!DOCTYPE html>
<html lang="en">
<head>
<meta charset="utf-8">
<title>Hemp Glide – Topical Vellor Wellworks</title>
<link rel="stylesheet" href="https://fonts.googleapis.com/css2?family=Cabin:wght@400;600;700&display=swap">
<style>
  :root{
    --page:#fafafa;
    --night:#1a060c;
    --ember:#b8290f;
    --flame:#f07a1c;
    --gold:#f2c21c;
    --leaf:#4f6a22;
    --leaf-dark:#2f4317;
    --ink:#0a0a0a;
    --white:#ffffff;
    --lime:#7cd63a;
    --grey:#c9c9c9;
  }
  *{box-sizing:border-box;margin:0;padding:0}
  html,body{width:1200px;height:1200px;overflow:hidden;background:var(--page)}
  .canvas{position:relative;width:1200px;height:1200px;font-family:"Cabin",sans-serif}

  .art-bg{position:absolute;inset:0;
    background:
      radial-gradient(ellipse 38% 30% at 22% 22%, rgba(240,122,28,.85), transparent 70%),
      radial-gradient(ellipse 30% 25% at 55% 48%, rgba(242,194,28,.35), transparent 70%),
      radial-gradient(ellipse 50% 40% at 80% 20%, rgba(184,41,15,.55), transparent 70%),
      linear-gradient(160deg,#3a0a10 0%,var(--night) 60%,#12030a 100%);}
  .leaf-area{position:absolute;left:10%;right:10%;top:2%;bottom:0;
    background:radial-gradient(ellipse 50% 48% at 50% 55%, rgba(79,106,34,.85), rgba(47,67,23,.55) 55%, transparent 75%);}

  .wordmark{position:absolute;left:0;right:0;text-align:center;color:var(--gold);
    font-family:"Cabin",sans-serif;font-weight:700;line-height:.95;letter-spacing:-2px}

  .box-front{position:absolute;left:90px;top:70px;width:1020px;height:680px;overflow:hidden;
    box-shadow:0 10px 30px rgba(0,0,0,.35)}
  .box-front .tagline{position:absolute;top:30px;left:0;right:0;text-align:center;
    color:var(--white);font-size:56px;letter-spacing:-1px}
  .box-front .wordmark{top:150px;font-size:190px}
  .box-front .claim{position:absolute;bottom:26px;left:0;right:0;text-align:center;
    color:var(--white);font-size:54px;letter-spacing:-1px}

  .label{position:absolute;top:785px;width:480px;height:380px;overflow:hidden;
    box-shadow:0 8px 22px rgba(0,0,0,.3)}
  .label-back{left:90px;background:var(--ink);color:var(--white);padding:18px 24px;font-size:15px;line-height:1.3}
  .label-back .head{color:var(--lime);font-weight:700;font-size:18px;margin-bottom:6px}
  .label-back .key{color:var(--lime)}
  .label-back p{margin-bottom:5px}
  .badges{display:flex;justify-content:space-between;margin:8px 0 6px}
  .badge{display:flex;flex-direction:column;align-items:center;width:25%;font-size:10px;font-weight:700;color:var(--gold)}
  .badge i{width:30px;height:30px;border-radius:50%;border:2px solid var(--lime);margin-bottom:4px}
  .label-back .small{font-size:11px;color:var(--grey)}
  .label-back .warn{color:var(--lime);font-weight:700;font-size:17px;margin:6px 0;border-bottom:1px solid var(--lime);padding-bottom:4px}
  .label-back .fda{border:1px solid var(--grey);padding:4px 8px;font-size:12px;color:var(--grey);margin-bottom:0}

  .label-front{left:630px}
  .label-front .tagline{position:absolute;top:16px;left:0;right:0;text-align:center;color:var(--white);font-size:22px}
  .label-front .wordmark{top:58px;font-size:84px;letter-spacing:-1px}
  .label-front .claim{position:absolute;top:262px;left:0;right:0;text-align:center;color:var(--white);font-size:20px;font-weight:600}
  .label-front .spec{position:absolute;top:292px;left:0;right:0;text-align:center;color:var(--grey);font-size:16px;letter-spacing:1px;line-height:1.4}
  .label-front .volume{position:absolute;top:340px;left:90px;right:90px;height:30px;background:var(--gold);
    text-align:center;font-weight:700;font-size:20px;line-height:30px;color:var(--ink)}
</style>
</head>
<body>
<div class="canvas">

  <section class="box-front">
    <div class="art-bg" role="img" aria-label="Fiery orange and red abstract glow background"></div>
    <div class="leaf-area" role="img" aria-label="Large green hemp leaf illustration behind the name"></div>
    <p class="tagline">TOPICAL VELLOR WELLWORKS</p>
    <h1 class="wordmark">HEMP<br>GLIDE</h1>
    <p class="claim">PENETRATES THROUGH THE SKIN</p>
  </section>

  <section class="label label-back">
    <p class="head">SHAKE WELL BEFORE USING</p>
    <p><span class="key">SUGGESTED USE:</span> Twice daily or as needed.</p>
    <p><span class="key">STORAGE:</span> Keep away from heat, light, and humidity to preserve freshness.</p>
    <p><span class="key">CAUTION:</span> Do not exceed suggested use. If you experience any adverse symptoms after use, please discontinue and consult your doctor.</p>
    <div class="badges">
      <span class="badge"><i></i>LAB TESTED</span>
      <span class="badge"><i></i>GLUTEN FREE</span>
      <span class="badge"><i></i>PURE ORGANIC</span>
      <span class="badge"><i></i>NON-GMO</span>
    </div>
    <p class="small">THIS PRODUCT IS NOT INTENDED TO DIAGNOSE, TREAT, CURE, OR PREVENT ANY DISEASE.</p>
    <p class="warn">KEEP OUT OF REACH OF CHILDREN</p>
    <p class="fda">These statements have not been evaluated by the Food &amp; Drug Administration.</p>
  </section>

  <section class="label label-front">
    <div class="art-bg" role="img" aria-label="Fiery orange and red abstract glow background"></div>
    <div class="leaf-area" role="img" aria-label="Green hemp leaf illustration behind the name"></div>
    <p class="tagline">TOPICAL VELLOR WELLWORKS</p>
    <h2 class="wordmark">HEMP<br>GLIDE</h2>
    <p class="claim">PENETRATES THROUGH THE SKIN</p>
    <p class="spec">PREMIUM FULL SPECTRUM<br>CANNABIDIOL OIL</p>
    <p class="volume">30ml (1oz)</p>
  </section>

</div>
</body>
</html>
```